Larkspur Homes - wanted BRILLIANT website design for our new property investing company

We need a website design for our new company based in Bristol, England, UK called "Larkspur Homes". We help buy people property who are in financial difficulty or who are needing to sell their property quickly for reasons such as death, divorce/separation, relocation, emigration.

We have a logo being designed incorporating strawberry and property (so red and green). We would like designs to communicate an elegant ,professional, approachable, friendly
fresh clean but also warm appealing appearance
Not too busy
Website consistent with logo and company name i.e. colour scheme

Please use our word document for content as a guide but use professional judgement for minor alterations if you feel they would benefit the site/structure etc

Please ask at any time if not sure

Target Market(s)

Adult british population, those that have a mortgage / loan / own property

Industry/Entity Type

Financial

Font styles to use
Serif
Sans Serif
Decorative

Colors
0692cd
33b7a4
acd036
fbee3e
3176b5
886aae
a6479a
e567a6
eb1f27

Requirements
Must have
• This must not look like a template website we are looking for UNIQUE please!
Nice to have
• Bristol pictures instead of generic, or colourful line drawings/comic drawings of houses/property/keys/happy people.....
Should not have
• An obvious off the shelf template design

```html
<!DOCTYPE html>
<html lang="en">
<head>
<meta charset="utf-8">
<title>Larkspur Homes</title>
<link href="https://fonts.googleapis.com/css2?family=Oswald:wght@400;500&family=Bebas+Neue&family=Libre+Baskerville:wght@700&family=Open+Sans:wght@400;600&family=Roboto+Condensed&display=swap" rel="stylesheet">
<style>
:root{
  --red:#c8232c;
  --red-dark:#b81f27;
  --green:#8dc21f;
  --green-dark:#7aad13;
  --blue:#0a72bf;
  --orange:#fbb217;
  --purple:#a340a0;
  --step-blue:#0a7bc7;
  --pink:#d83b86;
  --cream:#fffde8;
  --field:#fffde6;
  --text:#333;
  --muted:#555;
  --footer:#e9e9e9;
  --footer-bar:#5a5a5a;
}
*{margin:0;padding:0;box-sizing:border-box}
html,body{width:755px;height:1200px;overflow:hidden;background:#fff}
body{position:relative;font-family:Arial,Helvetica,sans-serif;color:var(--text)}
.abs{position:absolute}

/* header */
.header{left:0;top:0;width:755px;height:242px;background:linear-gradient(#d8eef2,#eef8f5 55%,#fff)}
.brand{left:22px;top:48px;display:flex;align-items:center;gap:10px}
.brand-dot{width:38px;height:38px;border-radius:50%;background:var(--red)}
.brand-name{font-family:"Libre Baskerville",serif;font-weight:700;font-size:25px;color:var(--red)}
.weather{left:540px;top:14px;width:68px;height:42px;border-radius:22px;background:radial-gradient(circle at 70% 35%,#f6c21c 0 28%,transparent 30%),linear-gradient(#fff,#e8eef0)}
.contact-top{right:28px;top:35px;text-align:right}
.contact-top .lead{font-size:9.5px;font-weight:bold;color:var(--red)}
.contact-top .phone{font-family:Oswald,sans-serif;font-weight:500;font-size:29px;color:var(--red);line-height:1.15}
.contact-top .mail{font-size:9.5px;color:#4a9a2a}
.houses{left:0;top:118px;width:755px;height:124px;background:linear-gradient(90deg,#f0e6c8,#d9744a 15%,#f5ecd5 30%,#c9633d 45%,#f3e9d3 60%,#e58b3d 75%,#f2e8cf 90%,#c86b44)}

/* nav */
.nav{left:0;top:242px;width:755px;height:28px;background:var(--red);display:flex;align-items:stretch;padding-left:5px}
.nav a{font-family:"Libre Baskerville",serif;font-size:9.2px;color:#fff;text-decoration:none;display:flex;align-items:center;padding:0 12.2px;text-transform:uppercase;font-weight:400}
.nav a.active{background:var(--green);padding:0 17px;margin-top:-2px}

/* hero */
.hero{left:0;top:270px;width:755px;height:308px;background:var(--cream)}
.headline{left:19px;top:300px;font-family:"Bebas Neue",sans-serif;font-size:40px;line-height:36px;color:var(--red);letter-spacing:-0.3px}
.intro{left:19px;top:384px;font-size:14px;color:#444}
.checklist{list-style:none;font-size:11.2px;color:#444}
.checklist li{position:relative;padding-left:16px;margin-bottom:6.5px;line-height:11px}
.checklist li::before{content:"";position:absolute;left:0;top:2px;border-left:6px solid var(--orange);border-top:3.5px solid transparent;border-bottom:3.5px solid transparent}
.list-a{left:29px;top:419px;width:170px}
.list-b{left:239px;top:419px;width:200px}

/* form */
.form-box{left:494px;top:306px;width:238px;height:255px;background:var(--green);border-radius:3px}
.ribbon{left:532px;top:295px;width:168px;height:40px;background:var(--blue);clip-path:polygon(0 0,100% 0,90% 100%,10% 100%);color:#fff;text-align:center}
.ribbon b{display:block;font-family:Oswald,sans-serif;font-weight:500;font-size:14px;padding-top:3px;letter-spacing:.5px}
.ribbon span{display:block;font-size:11px;margin-top:-2px}
.field{left:511px;width:204px;height:23px;background:var(--field);font-family:"Libre Baskerville",serif;font-size:10px;color:#444;padding:6px 8px}
.field.msg{height:71px}
.submit{left:511px;top:523px;width:204px;height:23px;background:var(--blue);color:#fff;font-family:"Libre Baskerville",serif;font-size:10.5px;text-align:center;line-height:23px}

/* steps */
.step{top:628px;width:138px;height:184px;color:#fff;padding:28px 8px 0 22px}
.step h3{font-family:Oswald,sans-serif;font-weight:400;font-size:13.5px;line-height:17px;margin-bottom:6px;text-transform:uppercase}
.step p{font-family:"Roboto Condensed",sans-serif;font-size:8.6px;line-height:12.5px}
.step p+p{margin-top:12px}
.s1{left:43px;background:var(--orange)}
.s2{left:181px;background:var(--purple)}
.s3{left:318px;background:var(--step-blue);top:620px;height:192px}
.s4{left:455px;background:var(--pink)}
.s5{left:592px;background:var(--green);width:137px;top:628px}
.num{top:602px;width:52px;height:52px;border-radius:50%;background:#fff;border:5px solid;font-family:Oswald,sans-serif;font-size:27px;line-height:40px;text-align:center}
.n1{left:17px;border-color:var(--orange);color:var(--orange)}
.n2{left:155px;border-color:var(--purple);color:var(--purple)}
.n3{left:292px;border-color:var(--step-blue);color:var(--step-blue)}
.n4{left:430px;border-color:var(--pink);color:var(--pink)}
.n5{left:567px;border-color:var(--green);color:var(--green)}

/* help */
.help-title{left:27px;top:842px;font-family:"Libre Baskerville",serif;font-weight:700;font-size:27px;color:#2a2a2a}
.help-list{list-style:none;font-family:"Open Sans",sans-serif;font-size:11.5px;color:#333;top:895px}
.help-list li{height:26px;padding-left:11px;position:relative}
.help-list li::before{content:"›";position:absolute;left:0;top:-2px;color:var(--red);font-weight:600}
.h1{left:36px}.h2{left:210px}.h3{left:385px}.h4{left:606px}

/* footer */
.footer{left:0;top:1028px;width:755px;height:137px;background:var(--footer)}
.foot-brand{left:22px;top:1094px;font-family:"Libre Baskerville",serif;font-weight:700;font-size:12.5px;color:#555}
.foot-h{top:1054px;font-family:"Open Sans",sans-serif;font-weight:600;font-size:14px;color:#333;letter-spacing:.4px}
.foot-links{list-style:none;font-size:8.8px;color:#444;line-height:11.2px;top:1082px}
.badge{top:1082px;height:30px;background:#7a7a7a;border-radius:3px}
.foot-phone{left:601px;top:1081px;font-family:"Open Sans",sans-serif;font-size:14px;color:#444;letter-spacing:.5px}
.foot-mail{left:602px;top:1101px;font-size:9.2px;color:#444}
.bottom{left:0;top:1165px;width:755px;height:35px;background:var(--footer-bar)}
.copy{left:20px;top:1180px;font-size:9px;color:#ddd}
.social{top:1174px;width:18px;height:18px;border-radius:50%;background:#c9c9c9}
</style>
</head>
<body>

<header class="abs header">
  <div class="abs brand"><span class="brand-dot"></span><span class="brand-name">Larkspur Homes</span></div>
  <div class="abs weather" role="img" aria-label="Illustration of a sun behind a small cloud"></div>
  <div class="abs contact-top">
    <div class="lead">For questions call us</div>
    <div class="phone">0117-4832</div>
    <div class="mail">info@larkspur-homes.co.uk</div>
  </div>
  <div class="abs houses" role="img" aria-label="Colourful illustrated row of terraced houses with tiled roofs"></div>
</header>

<nav class="abs nav">
  <a class="active">Home</a>
  <a>Sell your property fast</a>
  <a>Rent your property fast</a>
  <a>The 5 easy stpes</a>
  <a>Common questions</a>
  <a>About us</a>
  <a>Contact</a>
</nav>

<section class="abs hero"></section>
<h1 class="abs headline">Do youwant to sell or rent out<br>your house quickly?</h1>
<p class="abs intro">We are a local family run property business who specialize in</p>
<ul class="abs checklist list-a">
  <li>Buying properties quickly</li>
  <li>Finding creative solutions to your property problems</li>
  <li>Property rental management</li>
  <li>STOPPING repossession</li>
  <li>Motivated sellers</li>
</ul>
<ul class="abs checklist list-b">
  <li>Lettings to professional and student tenants</li>
  <li>Guaranteed rent and anagement schemes for landlord</li>
  <li>Chain fixing</li>
  <li>Negative equity problem</li>
</ul>

<div class="abs form-box"></div>
<div class="abs ribbon"><b>REQUEST</b><span>Free Evaluation</span></div>
<div class="abs field" style="top:347px">Name *</div>
<div class="abs field" style="top:373px">Email *</div>
<div class="abs field" style="top:398px">Phone Number *</div>
<div class="abs field" style="top:424px">Property Address *</div>
<div class="abs field msg" style="top:449px">Message</div>
<div class="abs submit">Submit</div>

<div class="abs step s1"><h3>Contact us</h3><p>Call our friendly team anytime OR fill in your contact details (above).</p><p>We will take your details and one of our expert team will be in contact within 48hrs. Usually within a very short</p></div>
<div class="abs step s2"><h3>Free consultation</h3><p>This is at a suitable time for yourself in your own home. We can view the property and have preliminary discussions into your problem and possible solutions.</p></div>
<div class="abs step s3"><h3>Guranteed offer</h3><p>We will organize a formal RPVS (Registered Property Valuers Society) valuation. This is to protect you and us and ensure we have an accurate valuation of your home.</p><p>At this point we can give you a guaranteed</p></div>
<div class="abs step s4"><h3>Legal stuff</h3><p>There will be paperwork to fill</p><p>Solicitors from both sides (yours and ours) will ensure the deal is made into a formal contract</p></div>
<div class="abs step s5"><h3>Completion and money in bank</h3><p>Contracts are exchanged Completion date arranged Your problems are solve</p></div>
<div class="abs num n1">1</div>
<div class="abs num n2">2</div>
<div class="abs num n3">3</div>
<div class="abs num n4">4</div>
<div class="abs num n5">5</div>

<h2 class="abs help-title">Who Can we Help?</h2>
<ul class="abs help-list h1"><li>How to stop repossession</li><li>Divorce or separation</li><li>Financial problems</li><li>Chain Collapse</li></ul>
<ul class="abs help-list h2"><li>Don’t like estate agents?</li><li>Property needing work</li><li>Retiring landlords</li><li>Tenanted Property</li></ul>
<ul class="abs help-list h3"><li>Negative equity</li><li>Opportunity not to be missed!!</li><li>Guaranteed rent scheme</li></ul>
<ul class="abs help-list h4"><li>Ill health</li><li>Relocating</li><li>Inherited property</li></ul>

<footer class="abs footer"></footer>
<div class="abs foot-brand">Larkspur Homes</div>
<div class="abs foot-h" style="left:177px">SITE NAV</div>
<ul class="abs foot-links" style="left:177px"><li>Home</li><li>Sell Your Property Fast</li><li>Rent Your Property Fast</li><li>The 5 Easy Stpes</li></ul>
<ul class="abs foot-links" style="left:294px"><li>Common Questions</li><li>About Us</li><li>Contact</li></ul>
<div class="abs foot-h" style="left:421px">AFFILIATED ORGS</div>
<div class="abs badge" style="left:416px;width:42px;border-radius:50%;height:42px;top:1078px"></div>
<div class="abs badge" style="left:468px;width:40px;height:44px;top:1078px"></div>
<div class="abs badge" style="left:514px;width:67px;height:22px;top:1090px"></div>
<div class="abs foot-h" style="left:601px">Call us free on</div>
<div class="abs foot-phone">0117 483290</div>
<div class="abs foot-mail">info@larkspur-homes.co.uk</div>

<div class="abs bottom"></div>
<div class="abs copy">© 2014 Larkspur Homes Limited. Reg No 7712368</div>
<span class="abs social" style="left:618px"></span>
<span class="abs social" style="left:642px"></span>
<span class="abs social" style="left:666px"></span>
<span class="abs social" style="left:690px"></span>
<span class="abs social" style="left:714px"></span>

</body>
</html>
```